Cybersecurity Start-Up - Korvelo

We need a power-point design for a new company based in Madrid (Spain) called 'Korvelo'. We aim to provide cybersecurity services to small- medium size companies for whom security is critical but paying big money to huge companies is not affordable.

The final design should communicate several things. As technology company which provides cybersecurity, it should be seen as something modern and futuristic , combined with safety and protection.

The company name Korvelo comes from Numantia, an ancient Celtiberian settlement in Spain which is famous for its role in the Celtiberian Wars (130 BC). They fought with Rome for 20 years , while being numerical inferior. And they won several times. When a final siege ocurred after a massive deployment of Rome legions, they held their ground for more than a year without food. When the situation was not longer sustainable, they decided to commit suicide rather than become slaves.

So the vision to hold the ground no matter what, should be communicated too
Updates

Need extra days to review

Requirements
Must have
• Check files attached for the logo of the company

```html
<!DOCTYPE html>
<html lang="en">
<head>
<meta charset="UTF-8">
<title>Korvelo – Slide</title>
<link href="https://fonts.googleapis.com/css2?family=Titillium+Web:wght@400;600&display=swap" rel="stylesheet">
<style>
  :root {
    --header-red: #e63e1b;
    --header-orange: #f4712b;
    --accent-orange: #e8770f;
    --rule-orange: #f28a1e;
    --footer-orange: #f7941d;
    --body-grey: #4f4f4f;
    --white: #ffffff;
  }
  * { margin: 0; padding: 0; box-sizing: border-box; }
  html, body { width: 1200px; height: 900px; overflow: hidden; background: var(--white); }
  .slide {
    position: relative;
    width: 1200px;
    height: 900px;
    font-family: "Titillium Web", sans-serif;
    background: var(--white);
    overflow: hidden;
  }
  .slide-header {
    position: absolute;
    top: 0; left: 0;
    width: 1200px; height: 95px;
  }
  .header-artwork {
    position: absolute;
    inset: 0;
    background: linear-gradient(90deg, var(--header-red) 0%, #ea4a20 45%, var(--header-orange) 75%, #ef5a24 100%);
  }
  .header-rule {
    position: absolute;
    top: 98px; left: 0;
    width: 1200px; height: 4px;
    background: var(--rule-orange);
  }
  .slide-title {
    position: absolute;
    left: 26px; top: 16px;
    color: var(--white);
    font-size: 42px;
    font-weight: 600;
    line-height: 1.2;
  }
  .brand-name {
    position: absolute;
    right: 30px; top: 18px;
    color: var(--white);
    font-size: 44px;
    font-weight: 600;
    line-height: 1.2;
  }
  .points {
    position: absolute;
    left: 0; top: 170px;
    width: 1200px;
  }
  .point {
    position: relative;
    height: 196.5px;
  }
  .point-icon {
    position: absolute;
    left: 40px; top: 6px;
    width: 44px; height: 44px;
  }
  .point-title {
    position: absolute;
    left: 105px; top: 0;
    color: var(--accent-orange);
    font-size: 34px;
    font-weight: 400;
    line-height: 1.3;
  }
  .point-text {
    position: absolute;
    left: 105px; top: 45px;
    width: 1070px;
    color: var(--body-grey);
    font-size: 19.5px;
    line-height: 31.5px;
  }
  .slide-footer {
    position: absolute;
    left: 0; bottom: 0;
    width: 1200px; height: 33px;
    background: var(--footer-orange);
  }
  .copyright {
    position: absolute;
    left: 12px; top: 3px;
    color: var(--white);
    font-size: 18px;
    line-height: 1.5;
  }
</style>
</head>
<body>
<div class="slide">
  <header class="slide-header">
    <div class="header-artwork" role="img" aria-label="Orange-red banner image of a circuit board and lines of code"></div>
    <h1 class="slide-title">Project Title Here</h1>
    <div class="brand-name">Korvelo</div>
  </header>
  <div class="header-rule"></div>

  <main class="points">
    <section class="point">
      <svg class="point-icon" viewBox="0 0 44 44" aria-hidden="true">
        <path d="M8 23 L18 33 L38 9" fill="none" stroke="var(--accent-orange)" stroke-width="6" stroke-linecap="round" stroke-linejoin="round"/>
      </svg>
      <h2 class="point-title">Bullet Point Title Here</h2>
      <p class="point-text">Toffee caramels candy canes bonbon bonbon soufflé bonbon wafer. Topping I love halvah I love. Jujubes lemon drops I love jelly pie chocolate bar. Biscuit oat cake carrot cake. Muffin jelly beans chocolate chocolate. Sugar plum I love cheesecake marshmallow oreo cake sweet cookies topping jelly gummies.</p>
    </section>
    <section class="point">
      <svg class="point-icon" viewBox="0 0 44 44" aria-hidden="true">
        <path d="M8 23 L18 33 L38 9" fill="none" stroke="var(--accent-orange)" stroke-width="6" stroke-linecap="round" stroke-linejoin="round"/>
      </svg>
      <h2 class="point-title">Bullet Point Title Here</h2>
      <p class="point-text">Toffee caramels candy canes bonbon bonbon soufflé bonbon wafer. Topping I love halvah I love. Jujubes lemon drops I love jelly pie chocolate bar. Biscuit oat cake carrot cake. Muffin jelly beans chocolate chocolate. Sugar plum I love cheesecake marshmallow oreo cake sweet cookies topping jelly gummies.</p>
    </section>
    <section class="point">
      <svg class="point-icon" viewBox="0 0 44 44" aria-hidden="true">
        <path d="M8 23 L18 33 L38 9" fill="none" stroke="var(--accent-orange)" stroke-width="6" stroke-linecap="round" stroke-linejoin="round"/>
      </svg>
      <h2 class="point-title">Bullet Point Title Here</h2>
      <p class="point-text">Toffee caramels candy canes bonbon bonbon soufflé bonbon wafer. Topping I love halvah I love. Jujubes lemon drops I love jelly pie chocolate bar. Biscuit oat cake carrot cake. Muffin jelly beans chocolate chocolate. Sugar plum I love cheesecake marshmallow oreo cake sweet cookies topping jelly gummies.</p>
    </section>
  </main>

  <footer class="slide-footer">
    <span class="copyright">Copyright text here</span>
  </footer>
</div>
</body>
</html>
```